Fine Art business needs new website

We need a simple website with a home page, about us page, New sculptures, Sold sculptures, and a contact us page.Our sculptures are very high end one of a kind pieces. As such we need the site to be VERY elegant and professional. Lastly, because I'll be updating pictures on the website on a monthly basis it needs to be user friendly to update (Wordpress is preferred). The only branding we have so far for the business is a business card.
Updates
I wasn't completely ready when this project launched, also I am on the road right now and haven't been able to be as responsive to all you designers as I would like. I will work on giving feedback to all the top designs we've received so far. Thank you all so much for your participation and hardwork.
Target Market(s)
High end customers (affluent), art collectors, interior decorators/designers
Industry/Entity Type
Art Gallery
Coding
Coded - Design and coding required
Number of Pages Required
5+ page
Requirements
Must have
- Easily editable picture gallery for myself so that I can add new pieces(pictures of the pieces), remove sold pieces, etc. I would like the website to be built in wordpress so I can update it. I currently use sitekeeperpro through Netbirch for my other business website and would like to do the same for this one.
- Pages:
- -Intro page with featured pieces
- -Current pieces gallery (for sale) mainly a picture gallery
- -Sculptures archive (sold pieces) another picture gallery
- -About us: Pull-down of -about the artist (attached content)
- -Artistic Process (attached content)
- -Show Schedule:
- -one page dedicated to "friends of QMW" (basically a link page)
- TO BE CLEAR "www.lanternhollow.com" IS A TOTALLY DIFFERENT SITE AND I'M NOT TRYING TO COMBINE THE TWO OR JOIN THEM INTO ONE. This page needs be more elegant and seperate from the Lantern Hollow site.
- UPDATE: I'd like a link to the QMW Friendsheet page: https://www.facebook.com/quillmarkworks/
Nice to have
- I would like the pictures on the gallery pages able to have text connected with them (Materials, price)
- I would like the site style and fonts to be similar to our business cards we've already had designed (picture attached).
Should not have
- Too much flash or other things that will make the site slow to load.

```html
<!DOCTYPE html>
<html lang="en">
<head>
<meta charset="utf-8">
<title>Quill Mark Works</title>
<link rel="stylesheet" href="https://fonts.googleapis.com/css2?family=Cormorant+Garamond:wght@400;500;700&family=Karla:wght@400;500&display=swap">
<style>
  :root {
    --white: #ffffff;
    --ink: #111111;
    --text-grey: #555555;
    --rule: #dddddd;
    --gallery-tone: #a9acd6;
    --studio-tone: #c8d5da;
    --piece-tone: #b9ada0;
    --copyright-band: #ddedf4;
    --social: #3b4a8c;
  }
  * { margin: 0; padding: 0; box-sizing: border-box; }
  html, body { width: 1200px; height: 1000px; overflow: hidden; background: var(--white); }
  body { position: relative; font-family: "Karla", Arial, sans-serif; color: var(--ink); }

  .featured-piece { position: absolute; top: 0; left: 0; width: 1200px; height: 142px; }
  .piece-details { position: absolute; right: 634px; top: 14px; text-align: right; }
  .piece-materials { font-family: "Cormorant Garamond", Georgia, serif; font-size: 15px; color: var(--text-grey); }
  .piece-price { font-family: "Cormorant Garamond", Georgia, serif; font-weight: 700; font-size: 26px; margin-top: 18px; }
  .piece-photo { position: absolute; left: 600px; top: 0; width: 600px; height: 142px;
    background: linear-gradient(180deg, #c8bfb6, var(--piece-tone)); }

  .promo-row { position: absolute; top: 214px; left: 0; width: 1200px; height: 411px; display: flex; }
  .promo-panel { width: 600px; height: 411px; text-align: center; padding-top: 140px; }
  .promo-panel.gallery { background: linear-gradient(135deg, #b3b5dd, var(--gallery-tone)); }
  .promo-panel.studio { background: linear-gradient(135deg, #d3ddd6, var(--studio-tone)); }
  .promo-title { font-family: "Cormorant Garamond", Georgia, serif; font-weight: 400; font-size: 41px; letter-spacing: 1.5px; line-height: 1; }
  .promo-text { font-size: 13px; line-height: 18px; margin: 18px auto 0; width: 460px; }
  .promo-button { display: inline-block; margin-top: 28px; width: 190px; height: 30px; line-height: 30px;
    background: var(--white); font-size: 10px; letter-spacing: 1.5px; text-transform: uppercase; color: var(--ink);
    text-decoration: none; box-shadow: 0 1px 3px rgba(0,0,0,.12); }

  .site-footer { position: absolute; top: 696px; left: 0; width: 1200px; height: 250px; border-top: 2px solid var(--rule); }
  .footer-sculpture { position: absolute; border-radius: 40% 40% 10% 10%; }
  .footer-sculpture.left { left: 70px; top: 26px; width: 100px; height: 200px; background: linear-gradient(180deg, #5a3a9a, #3c2a70 70%, #4b4b4b); }
  .footer-sculpture.right { left: 1034px; top: 26px; width: 78px; height: 200px; background: linear-gradient(180deg, #7a5a48, #5a4a55 70%, #4b4b4b); }
  .brand-name { text-align: center; font-family: "Cormorant Garamond", Georgia, serif; font-size: 33px; letter-spacing: 1.5px; color: var(--text-grey); margin-top: 22px; }
  .footer-nav { display: flex; justify-content: center; margin-top: 27px; font-size: 14px; letter-spacing: .4px; }
  .footer-nav a { color: var(--ink); text-decoration: none; }
  .footer-nav .divider { margin: 0 12px; }
  .footer-contact { display: flex; justify-content: center; gap: 14px; margin-top: 35px; font-size: 14px; color: var(--text-grey); }
  .footer-contact span { display: inline-flex; align-items: center; gap: 4px; }
  .footer-social { display: flex; justify-content: center; gap: 18px; margin-top: 39px; font-size: 13px; color: var(--social); }
  .copyright { position: absolute; top: 946px; left: 0; width: 1200px; height: 54px; background: var(--copyright-band);
    text-align: center; line-height: 54px; font-size: 13px; color: var(--text-grey); }
</style>
</head>
<body>
  <section class="featured-piece">
    <div class="piece-details">
      <p class="piece-materials">Amethyst Crystal, Gold Mounting Plates, Kauri Wood Base</p>
      <p class="piece-price">$1099.00</p>
    </div>
    <div class="piece-photo" role="img" aria-label="Polished spiral stone sculpture with amber crystal on a dark base"></div>
  </section>

  <section class="promo-row">
    <div class="promo-panel gallery" role="img" aria-label="Sculpture gallery booth with stone pieces on pedestals, purple tint">
      <h2 class="promo-title">SCULPTURE GALLERY</h2>
      <p class="promo-text">Lorem ipsum dolor sit amet, consectetur adipisicing elit, sed do eiusmod tempor incididunt ut labore et dolore magna aliqua. Ut enim ad minim</p>
      <a class="promo-button" href="#">Explore the gallery</a>
    </div>
    <div class="promo-panel studio" role="img" aria-label="Gloved hands holding an opened white geode, pale blue tint">
      <h2 class="promo-title">INSIDE THE STUDIO</h2>
      <p class="promo-text">Lorem ipsum dolor sit amet, consectetur adipisicing elit, sed do eiusmod tempor incididunt ut labore et dolore magna aliqua. Ut enim ad minim</p>
      <a class="promo-button" href="#">About us</a>
    </div>
  </section>

  <footer class="site-footer">
    <div class="footer-sculpture left" role="img" aria-label="Purple amethyst crystal sculpture on a granite base"></div>
    <div class="footer-sculpture right" role="img" aria-label="Brown crystal cluster sculpture on a granite base"></div>
    <p class="brand-name">QUILL MARK WORKS</p>
    <nav class="footer-nav">
      <a href="#">Gallery</a><span class="divider">|</span>
      <a href="#">Archive</a><span class="divider">|</span>
      <a href="#">About</a><span class="divider">|</span>
      <a href="#">Artistic Process</a><span class="divider">|</span>
      <a href="#">Show Schedule</a><span class="divider">|</span>
      <a href="#">Friendsheet</a><span class="divider">|</span>
      <a href="#">Friends of QMW</a>
    </nav>
    <div class="footer-contact">
      <span>
        <svg width="10" height="12" viewBox="0 0 10 12" aria-hidden="true"><path d="M2 0.5 L4 3 L3 4.5 Q4 7 5.5 8.5 L7 7.5 L9.5 9.5 L8 11.5 Q3 10.5 0.5 2 Z" fill="#555"/></svg>
        (555) 204-3318
      </span>
      <span>
        <svg width="13" height="10" viewBox="0 0 13 10" aria-hidden="true"><rect x="0.5" y="0.5" width="12" height="9" fill="#555"/><path d="M0.5 0.5 L6.5 5.5 L12.5 0.5" fill="none" stroke="#fff" stroke-width="1"/></svg>
        ellis@lanternhollow.com
      </span>
    </div>
    <div class="footer-social">
      <span>Circlepost</span>
      <span>Snapframe</span>
      <span>Friendsheet</span>
    </div>
  </footer>

  <div class="copyright">Copyright © 2018 Quill Mark Works. All rights reserved.</div>
</body>
</html>
```